Business Card Design

I'm looking for a cool business card design that showcases what my company does... I am the owner and Corvan is a play on my last name. The Corvan Group is a privately held entity that specializes in media (Corvan Media) and financial services (Corvan Trading).

Corvan Media focuses on the distribution and management of quality entertainment properties to all areas of the media world including broadcast, cable, digital, mobile and social media. Corvan Media helps media and entertainment companies create and market great content and ensure that it reaches the widest audience possible.

Corvan Media currently represents Glimmer TV (www.glimmertv-example.com), the fastest growing over the air broadcast network that focuses on programming that appeals to the African American audience. Corvan Media also represents two new over the air broadcast networks launching in Summer 2014 - Harbor TV (www.harbortv-example.com) and Plume TV (www.plumetv-example.com).

Corvan Media is an investor and business partner in SnapDrift (www.snapdrift-example.com) - a mobile social platform that empowers the user to choose how long your photos and videos live online.

Corvan Media also represents RMQ Enterprises (www.rmqent-example.com), an independent producer that creates talent-driven and cost-effective programming around emerging talent and Quillbright Content, a prolific producer of multimedia content including ZNK's hit program - Tundra Hall.

Corvan Trading manages a family office and focuses on building meaningful partnerships with all major financial institutions with a heavy concentration on IPO and secondary offerings.

Industry/Entity Type

Entertainment

Contact Information for Business Card

Marcus Pendle
12 Birchmere Lane
Marlow Ridge Ohio 44721
O 330.555.0143
C 330.555.0178

```html
<!DOCTYPE html>
<html lang="en">
<head>
<meta charset="utf-8">
<title>The Corvan Group – Business Card</title>
<link href="https://fonts.googleapis.com/css2?family=Lato:wght@400;700&display=swap" rel="stylesheet">
<style>
  :root {
    --backdrop: #3b3b3b;
    --card-white: #ffffff;
    --card-black: #0d0d0d;
    --accent-orange: #e07b22;
    --ink-dark: #1c1c1c;
    --brand-grey: #6f6a64;
    --contact-white: #f4f4f4;
  }
  * { box-sizing: border-box; margin: 0; padding: 0; }
  html, body {
    width: 1200px;
    height: 900px;
    overflow: hidden;
    background: var(--backdrop);
    font-family: "Lato", sans-serif;
  }
  .canvas {
    position: relative;
    width: 1200px;
    height: 900px;
  }
  .business-card {
    position: absolute;
    left: 75px;
    top: 150px;
    width: 1050px;
    height: 600px;
    background: var(--card-white);
    overflow: hidden;
    box-shadow: 0 18px 40px rgba(0,0,0,0.45);
  }
  .card-swoosh {
    position: absolute;
    inset: 0;
    width: 100%;
    height: 100%;
  }
  .swoosh-orange { fill: var(--accent-orange); }
  .swoosh-black { fill: var(--card-black); }

  .holder-name {
    position: absolute;
    right: 62px;
    top: 40px;
    font-size: 34px;
    font-weight: 400;
    color: var(--ink-dark);
    letter-spacing: 0.2px;
  }
  .holder-name .surname { font-weight: 700; }

  .brand-name {
    position: absolute;
    left: 70px;
    top: 262px;
    font-size: 50px;
    font-weight: 700;
    color: var(--brand-grey);
    letter-spacing: 1px;
    white-space: nowrap;
  }

  .contact-list {
    position: absolute;
    right: 62px;
    top: 388px;
    list-style: none;
    text-align: right;
    color: var(--contact-white);
    font-size: 22px;
    line-height: 36px;
    white-space: nowrap;
  }
  .contact-list .contact-key {
    color: var(--accent-orange);
    font-weight: 700;
    display: inline-block;
    width: 18px;
    text-align: right;
  }
</style>
</head>
<body>
<main class="canvas">
  <article class="business-card">
    <svg class="card-swoosh" viewBox="0 0 1050 600" preserveAspectRatio="none" aria-hidden="true">
      <path class="swoosh-orange" d="M0,535 Q500,485 1050,100 L1050,600 L0,600 Z"/>
      <path class="swoosh-black" d="M0,562 Q520,520 1050,150 L1050,600 L0,600 Z"/>
    </svg>

    <h1 class="holder-name">Marcus <span class="surname">Pendle</span></h1>

    <p class="brand-name">The Corvan Group</p>

    <ul class="contact-list">
      <li>330.555.0143 : <span class="contact-key">O</span></li>
      <li>330.555.0178 : <span class="contact-key">C</span></li>
      <li>12 Birchmere Lane Marlow Ridge Ohio 44721 : <span class="contact-key">A</span></li>
    </ul>
  </article>
</main>
</body>
</html>
```